Velmora Print House gallery website

I need a Website for a gallery with a shopify integration or maybe even better also compatible with squarespace.
the website should have following riders: Künstler, Veranstaltungen, Shop, About Us.
some nice examples for inspiration of the website architecture are:
https://www.trasselhausgalerie.com/
https://www.plovikwerk-gallery.com/de/
https://quendelmoorgalerie.de/
It should be easy for us to make adaptations and fill the website with new content.
Attached there is the CI an logo for the brand.
Target Market(s)
Art Collectors,
Industry/Entity Type
artgallery
Coding
Coded - Design and coding required
Number of Pages Required
3 page
Look and feel

```html
<!DOCTYPE html>
<html lang="de">
<head>
<meta charset="utf-8">
<title>Velmora Print House</title>
<link rel="stylesheet" href="https://fonts.googleapis.com/css2?family=Open+Sans:wght@400;600;700;800&family=Open+Sans+Condensed:wght@700&family=Raleway:wght@300;500&family=Playfair+Display:wght@400&display=swap">
<style>
  :root {
    --page: #ffffff;
    --hero-top: #f7f8fa;
    --hero-bottom: #e9ecef;
    --ink: #1d1d1f;
    --muted: #5c5f63;
    --faint: #9a9da1;
    --photo-light: #eef0f3;
    --photo-mid: #c9a987;
    --photo-dark: #8a6a4c;
  }
  * { box-sizing: border-box; margin: 0; padding: 0; }
  html, body { width: 1200px; height: 960px; overflow: hidden; background: var(--page); }
  body { font-family: "Open Sans", sans-serif; color: var(--ink); }

  .site { position: relative; width: 1200px; height: 960px; }

  .hero {
    position: relative;
    height: 650px;
    background: linear-gradient(180deg, var(--hero-top) 0%, var(--hero-bottom) 100%);
    overflow: hidden;
  }

  .hero-photo {
    position: absolute; left: 715px; top: 0; width: 380px; height: 650px;
    background:
      radial-gradient(ellipse 45% 55% at 55% 42%, var(--photo-light) 0%, rgba(238,240,243,0) 70%),
      linear-gradient(100deg, var(--photo-dark) 0%, var(--photo-mid) 35%, #e6dcd2 60%, var(--photo-light) 100%);
    opacity: 0.85;
  }

  .brand {
    position: absolute; left: 40px; top: 90px; width: 180px;
    text-align: center;
  }
  .brand-name {
    font-family: "Raleway", sans-serif; font-weight: 300;
    font-size: 17px; letter-spacing: 0.2px; color: var(--ink);
    white-space: nowrap;
  }
  .brand-city {
    font-family: "Raleway", sans-serif; font-weight: 300;
    font-size: 6px; letter-spacing: 3px; color: var(--ink); margin-top: 4px;
  }

  .main-nav {
    position: absolute; left: 434px; top: 30px; z-index: 2;
    display: flex; gap: 14px;
  }
  .main-nav a {
    font-size: 8px; font-weight: 600; letter-spacing: 0.8px;
    text-transform: uppercase; color: var(--ink); text-decoration: none;
  }

  .hero-copy { position: absolute; left: 100px; top: 445px; z-index: 2; }
  .hero-kicker {
    font-size: 8px; font-weight: 700; letter-spacing: 1px;
    text-transform: uppercase; color: var(--muted);
  }
  .hero-title {
    font-family: "Open Sans Condensed", "Open Sans", sans-serif; font-weight: 700;
    font-size: 48px; line-height: 1; margin-top: 14px; letter-spacing: 0.5px;
  }
  .hero-button {
    display: inline-block; margin-top: 30px; margin-left: 6px;
    background: var(--ink); color: #fff; text-decoration: none;
    font-size: 8px; font-weight: 700; letter-spacing: 1.2px;
    text-transform: uppercase; padding: 13px 24px;
  }

  .about { text-align: center; padding-top: 70px; }
  .about-label {
    font-size: 8px; letter-spacing: 1.2px; text-transform: uppercase; color: var(--faint);
  }
  .about-text {
    font-family: "Playfair Display", serif; font-size: 17px; line-height: 1.5;
    margin: 28px auto 0; width: 440px; color: var(--ink);
  }
</style>
</head>
<body>
<div class="site">
  <header class="hero">
    <div class="hero-photo" role="img" aria-label="Fashion portrait in profile with a braided blond ponytail and a dark paint stroke"></div>

    <div class="brand">
      <div class="brand-name">Velmora Print House</div>
      <div class="brand-city">HAMBURG</div>
    </div>

    <nav class="main-nav">
      <a href="#">Künstler</a>
      <a href="#">Veranstaltungen</a>
      <a href="#">About us</a>
      <a href="#">Shop</a>
    </nav>

    <div class="hero-copy">
      <p class="hero-kicker">Fashion photography</p>
      <h1 class="hero-title">VELTRANA</h1>
      <a class="hero-button" href="#">View portfolio</a>
    </div>
  </header>

  <section class="about">
    <p class="about-label">About us</p>
    <p class="about-text">My greatest ambition is to create powerful images that commemorate across generations, the people we love and the good</p>
  </section>
</div>
</body>
</html>
```